Letter head / email signature/ contract document templates

We need a professional email signature and letterhead designed for our established carpentry and maintenance company. Our Logo (attached) was originally designed 6 years ago by design guru and we love it, looking for something to compliment it ( not a home job)

```html
<!DOCTYPE html>
<html lang="en">
<head>
<meta charset="utf-8">
<title>Harbourline Maintenance – Stationery</title>
<link href="https://fonts.googleapis.com/css2?family=Lato:wght@400;700;900&family=Arimo:wght@400&display=swap" rel="stylesheet">
<style>
  :root{
    --backdrop:#8e8d91;
    --paper:#f1f1f2;
    --card:#ffffff;
    --red:#c8141c;
    --ink:#3a3a3c;
    --text:#2f2f31;
    --muted:#555557;
    --band:#3b3b3d;
    --sign:#cfcfd2;
  }
  *{margin:0;padding:0;box-sizing:border-box}
  html,body{width:1200px;height:858px;overflow:hidden;background:var(--backdrop)}
  body{position:relative;font-family:'Lato',sans-serif;color:var(--text)}
  .sheet,.card{position:absolute;overflow:hidden}
  .sheet{left:122px;top:65px;width:507px;height:713px;background:var(--paper);box-shadow:0 2px 6px rgba(0,0,0,.25)}
  .card{background:var(--card);box-shadow:0 2px 5px rgba(0,0,0,.25)}

  .brand{position:absolute;display:flex;align-items:center;gap:6px;font-family:'Lato',sans-serif;font-weight:900;color:var(--ink);line-height:1.02;letter-spacing:.2px}
  .brand-dot{width:9px;height:9px;background:var(--red);flex:none}

  .contact{position:absolute;font-family:'Lato',sans-serif;color:var(--muted)}
  .contact .row{display:flex;align-items:center;gap:5px;white-space:nowrap}
  .contact .icon{flex:none;fill:var(--red)}
  .contact .indent{padding-left:13px}

  .red-rule{position:absolute;left:0;right:0;background:var(--red)}
  .dark-band{position:absolute;left:0;right:0;bottom:0;background:var(--band);color:#fff;display:flex;align-items:center;justify-content:center}

  /* letterhead */
  .sheet .brand{left:35px;top:62px;font-size:15px;width:140px}
  .sheet .contact{left:360px;top:57px;font-size:7px;line-height:9.2px}
  .sheet .contact .gap{height:4px}
  .salutation{position:absolute;left:38px;top:178px;font-family:'Arimo',sans-serif;font-size:12.5px;color:#444}
  .letter-body{position:absolute;left:38px;top:215px;width:433px;font-family:'Arimo',sans-serif;font-size:7.05px;line-height:10.8px;color:#3d3d3f;text-align:justify}
  .letter-body p{margin-bottom:10.8px}
  .closing{position:absolute;left:38px;top:454px;font-family:'Arimo',sans-serif;font-size:7.2px;color:#3d3d3f}
  .signature{position:absolute;left:36px;top:478px;width:148px;height:42px;background:var(--sign);border-radius:3px}
  .sheet .red-rule{top:683px;height:5px}
  .sheet .dark-band{height:23px;font-size:8.5px;letter-spacing:2.4px}

  .name{position:absolute;color:var(--red);font-weight:700;font-size:13px;line-height:15px}
  .title{position:absolute;color:var(--text);font-size:9px}
  .divider{position:absolute;width:1px;background:var(--ink)}

  /* vertical card */
  .card-portrait{left:663px;top:207px;width:184px;height:280px}
  .card-portrait .brand{left:24px;top:34px;font-size:15px;width:140px}
  .card-portrait .name{left:26px;top:109px}
  .card-portrait .title{left:26px;top:125px}
  .card-portrait .contact{left:26px;top:164px;font-size:9px;line-height:11px}
  .card-portrait .gap{height:5px}
  .card-portrait .red-rule{top:261px;height:3px}
  .card-portrait .dark-band{height:14px;font-size:8.5px;justify-content:flex-start;padding-left:26px}

  /* landscape card */
  .card-landscape{left:660px;top:510px;width:416px;height:148px}
  .card-landscape .brand{left:52px;top:54px;font-size:16px;width:130px}
  .card-landscape .divider{left:195px;top:25px;height:90px}
  .card-landscape .name{left:229px;top:17px}
  .card-landscape .title{left:229px;top:33px}
  .card-landscape .contact{left:229px;top:48px;font-size:9px;line-height:11.2px}
  .card-landscape .gap{height:6px}
  .card-landscape .red-rule{top:135px;height:3px}
  .card-landscape .dark-band{height:9px}

  /* wide card */
  .card-wide{left:660px;top:680px;width:516px;height:120px}
  .card-wide .brand{left:39px;top:44px;font-size:15px;width:130px}
  .card-wide .divider.first{left:183px;top:19px;height:73px}
  .card-wide .divider.second{left:318px;top:19px;height:73px}
  .card-wide .name{left:210px;top:49px}
  .card-wide .title{left:210px;top:65px}
  .card-wide .contact{left:339px;top:17px;font-size:9px;line-height:11.2px}
  .card-wide .red-rule{top:107px;height:3px}
  .card-wide .dark-band{height:8px}
</style>
</head>
<body>

<svg width="0" height="0" style="position:absolute" aria-hidden="true">
  <defs>
    <symbol id="i-pin" viewBox="0 0 10 10"><path d="M5 0a3.6 3.6 0 0 0-3.6 3.6C1.4 6.2 5 10 5 10s3.6-3.8 3.6-6.4A3.6 3.6 0 0 0 5 0zm0 5a1.4 1.4 0 1 1 0-2.8A1.4 1.4 0 0 1 5 5z"/></symbol>
    <symbol id="i-phone" viewBox="0 0 10 10"><path d="M2.2.6 3.8 2.6 2.9 3.8c.6 1.4 1.8 2.6 3.3 3.3l1.2-.9 2 1.6-.9 1.6C4.6 9.2.8 5.4.6 1.5z"/></symbol>
    <symbol id="i-mobile" viewBox="0 0 10 10"><path d="M2.6 0h4.8v10H2.6zm1 1v7h2.8V1z"/></symbol>
    <symbol id="i-mail" viewBox="0 0 10 10"><path d="M0 2h10v6.5H0zm1 .9 4 3 4-3z"/></symbol>
    <symbol id="i-globe" viewBox="0 0 10 10"><circle cx="5" cy="5" r="4.6"/><path d="M3 2.5 4.8 3.4 4 5.4 5.8 6.6 5 8.6" stroke="#fff" stroke-width=".9" fill="none"/></symbol>
  </defs>
</svg>

<!-- Letterhead -->
<section class="sheet">
  <div class="brand"><span class="brand-dot"></span><span>Harbourline Maintenance</span></div>
  <div class="contact">
    <div class="row indent" style="padding-left:0">1420 Cedar Ridge Road</div>
    <div class="row" style="padding-left:0">Fairbanks, Alaska 34611</div>
    <div class="gap"></div>
    <div class="row"><svg class="icon" width="6" height="6"><use href="#i-phone"/></svg>555-204-7731</div>
    <div class="row"><svg class="icon" width="6" height="6"><use href="#i-mobile"/></svg>555-318-6642</div>
    <div class="row"><svg class="icon" width="6" height="6"><use href="#i-mail"/></svg>hello@harbourlinemaint.com</div>
  </div>

  <p class="salutation">Dear Mr. Reeves,</p>
  <div class="letter-body">
    <p>Lorem ipsum dolor sit amet, consectetur adipiscing elit. Donec orci purus, luctus vitae dignissim eu, iaculis sed purus. Vivamus faucibus, ipsum nec aliquet viverra, leo mauris condimentum ligula, sit amet sagittis enim ligula quis arcu. Nam egestas tortor id nisi porttitor mattis. In tortor ante, ultricies in suscipit a, tempus non massa. Vivamus et auctor mi. Fusce vel massa nulla. Phasellus nec eros mauris, et scelerisque orci.</p>
    <p>Donec malesuada orci vitae nulla accumsan porta a id massa. Quisque accumsan iaculis magna sit amet fringilla. Maecenas consequat, magna eget tincidunt semper, odio nibh rutrum mi, id feugiat ante nisi eu risus. Vestibulum nunc orci, rhoncus a placerat in, ultricies in mi. Cras mattis varius eros, vel fringilla nisi suscipit eget. Quisque scelerisque sagittis nulla at porttitor.</p>
    <p>Sed id augue vitae urna euismod commodo aliquet a quam. Pellentesque arcu velit, cursus et malesuada ut, consequat et diam. Nullam erat sem, rhoncus id ullamcorper vitae, rhoncus et arcu. In ultricies ultricies nulla, ut rutrum nisi iaculis at. Donec eu magna a metus ornare faucibus. Fusce aliquet faucibus ultricies. Morbi semper, est id tincidunt gravida, sem arcu adipiscing lacus, ac bibendum nulla leo eu purus. Quisque nec diam sed risus consectetur a cumsan quis quis nibh. Vestibulum id purus lorem.</p>
    <p>It is a long established fact that a reader will be distracted by the readable content of a page when looking at its layout. The point of using Lorem Ipsum is that it has a more-or-less normal distribution of letters, as opposed to using 'Content here, content here', making it look like readable English. Many desktop publishing packages</p>
    <p>ada ut, consequat et diam. Nullam erat sem, rhoncus id ullamcorper vitae, rhoncus et arcu. In ultricies ultricies nulla, ut rutrum nisi iaculis at. Donec eu magna a metus ornare faucibus. Fusce aliquet faucibus ultricies. Morbi semper,</p>
  </div>
  <p class="closing">Sincerely,</p>
  <div class="signature" role="img" aria-label="Handwritten signature"></div>

  <div class="red-rule"></div>
  <div class="dark-band">www.HarbourlineMaint.com</div>
</section>

<!-- Portrait business card -->
<section class="card card-portrait">
  <div class="brand"><span class="brand-dot"></span><span>Harbourline Maintenance</span></div>
  <p class="name">Daniel Reeves</p>
  <p class="title">President</p>
  <div class="contact">
    <div class="row"><svg class="icon" width="8" height="8"><use href="#i-pin"/></svg>1420 Cedar Ridge Road</div>
    <div class="row indent">Fairbanks, Alaska 34611</div>
    <div class="gap"></div>
    <div class="row"><svg class="icon" width="8" height="8"><use href="#i-phone"/></svg>555-204-7731</div>
    <div class="row"><svg class="icon" width="8" height="8"><use href="#i-mobile"/></svg>555-318-6642</div>
    <div class="row"><svg class="icon" width="8" height="8"><use href="#i-mail"/></svg>hello@harbourlinemaint.com</div>
  </div>
  <div class="red-rule"></div>
  <div class="dark-band">www.harbourlinemaint.com</div>
</section>

<!-- Landscape business card -->
<section class="card card-landscape">
  <div class="brand"><span class="brand-dot"></span><span>Harbourline Maintenance</span></div>
  <div class="divider"></div>
  <p class="name">Daniel Reeves</p>
  <p class="title">President</p>
  <div class="contact">
    <div class="row" style="margin-top:3px">1420 Cedar Ridge Road</div>
    <div class="row">Fairbanks, Alaska 34611</div>
    <div class="gap"></div>
    <div class="row"><svg class="icon" width="8" height="8"><use href="#i-phone"/></svg>555-204-7731</div>
    <div class="row"><svg class="icon" width="8" height="8"><use href="#i-mobile"/></svg>555-318-6642</div>
    <div class="row"><svg class="icon" width="8" height="8"><use href="#i-mail"/></svg>hello@harbourlinemaint.com</div>
    <div class="row"><svg class="icon" width="8" height="8"><use href="#i-globe"/></svg>harbourlinemaint.com</div>
  </div>
  <div class="red-rule"></div>
  <div class="dark-band"></div>
</section>

<!-- Wide email signature -->
<section class="card card-wide">
  <div class="brand"><span class="brand-dot"></span><span>Harbourline Maintenance</span></div>
  <div class="divider first"></div>
  <p class="name">Daniel Reeves</p>
  <p class="title">President</p>
  <div class="divider second"></div>
  <div class="contact">
    <div class="row"><svg class="icon" width="8" height="8"><use href="#i-pin"/></svg>1420 Cedar Ridge Road</div>
    <div class="row indent">Fairbanks, Alaska 34611</div>
    <div class="row"><svg class="icon" width="8" height="8"><use href="#i-phone"/></svg>555-204-7731</div>
    <div class="row"><svg class="icon" width="8" height="8"><use href="#i-mobile"/></svg>555-318-6642</div>
    <div class="row"><svg class="icon" width="8" height="8"><use href="#i-mail"/></svg>hello@harbourlinemaint.com</div>
    <div class="row"><svg class="icon" width="8" height="8"><use href="#i-globe"/></svg>www.harbourlinemaint.com</div>
  </div>
  <div class="red-rule"></div>
  <div class="dark-band"></div>
</section>

</body>
</html>
```